依頼詳細
(例)毎年忘年会・新年会チラシをうちます。その広告デザインをお願い致します。今年は新企画として女子会プランを紙面の半分のスペースに入れたいと思います。明るく楽しく見やすい和のデザインをお願いします。
記載項目
(例)入る原稿(文字、写真)はイラストレーターCS2にて添付します。裏面は昨年から流用しますので表面には住所や地図は入りません。タイトルをいじったりキャッチコピーを入れて下さってかまいません。
希望イメージ
シンプル 複雑
単色 カラフル
暗い 明るい
日常 高級
遊び心 厳粛
未来的 伝統的
女性的 男性的
希望する色
(例)赤、黒(特にこだわりません)
納品ファイル
• 高解像度JPG (.jpg)
• イラストレーター形式 (.ai)
補足説明
■ 選んだ理由

明るく楽しげな雰囲気がとてもよかったです。女子会のタイトルの工夫もいい感じです。

■ 提案者全員のお礼・コメント

多くの方に提案して頂きありがとうございました。1つ選ぶのは心苦しいのですが選んだ納得感が気に入っています。またお願いするときにはよろしくお願いします。

```html
<!DOCTYPE html>
<html lang="ja">
<head>
<meta charset="utf-8">
<title>和楽 忘年会・新年会 2012-2013</title>
<link href="https://fonts.googleapis.com/css2?family=Yuji+Syuku&family=Noto+Sans+JP:wght@400;700;900&family=Noto+Serif+JP:wght@700;900&family=Kiwi+Maru:wght@500&display=swap" rel="stylesheet">
<style>
  :root {
    --red: #c8161d;
    --deep-red: #8e0f14;
    --cream: #fdf6e3;
    --gold: #d8a93a;
    --ink: #3a2a1e;
    --pink: #e85a8a;
    --soft-pink: #fde6ee;
    --pale-pink: #fff3f7;
    --white: #ffffff;
  }
  html, body { margin: 0; padding: 0; overflow: hidden; background: #eee; }
  .flyer {
    position: relative; width: 823px; height: 1200px; overflow: hidden;
    background: var(--cream); font-family: "Noto Sans JP", sans-serif; color: var(--ink);
  }
  .abs { position: absolute; }

  /* ---------- year-end section ---------- */
  .top-frame { left: 0; top: 0; width: 823px; height: 660px; border-top: 10px solid var(--red); box-sizing: border-box; }
  .brand { left: 30px; top: 32px; display: flex; align-items: center; gap: 10px; }
  .brand-mark { width: 22px; height: 22px; border-radius: 50%; background: var(--red); }
  .brand-name { font-family: "Noto Serif JP", serif; font-weight: 900; font-size: 64px; color: var(--red); line-height: 1; }
  .party-art { left: 200px; top: 22px; width: 190px; height: 100px; border-radius: 12px;
    background: linear-gradient(135deg, #f6d9a8, #e9b56c); }

  .title { margin: 0; font-family: "Yuji Syuku", serif; color: var(--red); font-size: 114px; line-height: 1; letter-spacing: 2px; left: 24px; white-space: nowrap; }
  .title-bonen { top: 168px; }
  .title-shinnen { top: 330px; }
  .season { left: 200px; top: 290px; font-family: "Noto Serif JP", serif; font-weight: 900; font-size: 22px; color: var(--ink); white-space: nowrap; }

  .notes { margin: 0; left: 28px; top: 478px; width: 360px; font-size: 12px; line-height: 1.6; }
  .discount { left: 28px; top: 528px; display: flex; align-items: center; gap: 10px; }
  .discount-badge { background: var(--red); color: var(--white); font-weight: 900; font-size: 24px; padding: 2px 10px; }
  .discount-text { font-size: 12px; line-height: 1.5; }
  .bus { left: 28px; top: 582px; display: flex; align-items: center; gap: 12px; }
  .bus-text { font-weight: 900; font-size: 26px; color: var(--red); white-space: nowrap; }
  .bus-note { font-size: 12px; color: var(--ink); display: block; font-weight: 400; }

  .menu { left: 412px; top: 34px; width: 392px; }
  .menu-head { border-bottom: 3px solid var(--red); padding-bottom: 4px; font-weight: 700; font-size: 15px; color: var(--red); }
  .menu-head b { font-size: 30px; font-weight: 900; }
  .course { display: flex; gap: 8px; padding: 8px 0 6px; border-bottom: 1px dashed var(--gold); }
  .course-seal { flex: none; width: 40px; height: 40px; border-radius: 50%; background: var(--red); color: var(--white);
    font-family: "Noto Serif JP", serif; font-weight: 900; font-size: 24px; display: grid; place-items: center; }
  .course-name { font-weight: 700; font-size: 14px; }
  .course-name b { color: var(--red); font-size: 24px; font-weight: 900; margin-left: 6px; }
  .course-desc { font-size: 11px; line-height: 1.45; }

  .band { background: var(--deep-red); color: var(--white); font-family: "Noto Serif JP", serif; font-weight: 900;
    font-size: 24px; padding: 4px 14px; width: 200px; }
  .drinks-band { left: 412px; top: 386px; }
  .drinks-price { left: 412px; top: 430px; font-size: 13px; font-weight: 700; }
  .drinks-price b { font-size: 40px; color: var(--red); font-weight: 900; }
  .drinks-note { left: 412px; top: 484px; font-size: 11px; width: 210px; }
  .nabe-band { left: 412px; top: 528px; }
  .nabe-price { left: 412px; top: 570px; font-size: 13px; font-weight: 700; }
  .nabe-price b { font-size: 44px; color: var(--red); font-weight: 900; }
  .nabe-photo { left: 640px; top: 412px; width: 166px; height: 180px; border-radius: 50%;
    background: radial-gradient(circle at 50% 45%, #f3b15a, #b4452a 70%, #5a2616); }

  /* ---------- women's party section ---------- */
  .joshi { left: 0; top: 660px; width: 823px; height: 540px; background: var(--soft-pink); border-top: 6px solid var(--pink); box-sizing: border-box; }
  .joshi-kicker { left: 400px; top: 688px; font-family: "Kiwi Maru", serif; font-size: 26px; color: var(--pink); letter-spacing: 3px; }
  .joshi-title { margin: 0; left: 370px; top: 722px; font-family: "Kiwi Maru", serif; font-size: 74px; color: var(--pink); line-height: 1; white-space: nowrap; }
  .joshi-note { left: 470px; top: 806px; font-weight: 700; font-size: 16px; color: var(--ink); text-align: center; }

  .plan { background: var(--white); border: 3px solid var(--pink); border-radius: 14px; padding: 10px 14px; }
  .plan-name { font-family: "Kiwi Maru", serif; font-size: 22px; color: var(--pink); }
  .plan-price { font-weight: 900; font-size: 40px; color: var(--red); line-height: 1.1; }
  .plan-price small { font-size: 16px; }
  .plan-note { font-size: 11px; }
  .plan-sushi { left: 26px; top: 690px; width: 260px; }
  .plan-gozen { left: 568px; top: 1040px; width: 210px; }

  .side-dishes { left: 26px; top: 852px; width: 300px; height: 70px; display: flex; gap: 10px; }
  .side-dish { flex: 1; border-radius: 50%; background: radial-gradient(circle, #f7e2c4, #d79a6a); }
  .sushi-photo { left: 26px; top: 936px; width: 510px; height: 246px; border-radius: 16px;
    background: linear-gradient(135deg, #2c2a2a, #c84a3a 45%, #f2c9a0 75%, #3f5f3a); }
  .gozen-photo { left: 560px; top: 850px; width: 240px; height: 180px; border-radius: 16px;
    background: linear-gradient(135deg, #7a1f1f, #e3a77a 50%, #f6e6c8); }
</style>
</head>
<body>
<main class="flyer">
  <div class="abs top-frame"></div>

  <div class="abs brand"><span class="brand-mark"></span><span class="brand-name">和楽</span></div>
  <div class="abs party-art" role="img" aria-label="宴会を楽しむ人々のイラスト"></div>

  <h1 class="abs title title-bonen">忘年会</h1>
  <div class="abs season">2012・2013</div>
  <h1 class="abs title title-shinnen">新年会</h1>

  <p class="abs notes">3,500円以上のご予約で10名様以上のご来店の際、送迎バスを無料でご利用いただけます。</p>
  <div class="abs discount">
    <span class="discount-badge">5%OFF</span>
    <span class="discount-text">このチラシをお持ちの方は<br>ご会計より5%割引いたします。</span>
  </div>
  <div class="abs bus">
    <svg width="70" height="46" viewBox="0 0 70 46" aria-hidden="true">
      <rect x="2" y="4" width="64" height="32" rx="6" fill="#c8161d"/>
      <rect x="8" y="10" width="12" height="10" fill="#fff"/>
      <rect x="24" y="10" width="12" height="10" fill="#fff"/>
      <rect x="40" y="10" width="12" height="10" fill="#fff"/>
      <circle cx="16" cy="38" r="6" fill="#3a2a1e"/>
      <circle cx="52" cy="38" r="6" fill="#3a2a1e"/>
    </svg>
    <span class="bus-text">バス送迎ご利用下さい。<span class="bus-note">15名様以上で送迎いたします</span></span>
  </div>

  <section class="abs menu">
    <div class="menu-head">法要後のお食事宴会用会席料理 <b>3,500</b>円より</div>
    <div class="course"><div class="course-seal">雅</div><div><div class="course-name">雅 <b>3,500円</b></div><div class="course-desc">前菜・造り・焼物・煮物・揚物・茶碗蒸し・寿司・赤だし・デザート</div></div></div>
    <div class="course"><div class="course-seal">鶴</div><div><div class="course-name">鶴 <b>4,000円</b></div><div class="course-desc">前菜・造り盛合せ・焼物・煮物・揚物・酢物・寿司・吸物・デザート</div></div></div>
    <div class="course"><div class="course-seal">亀</div><div><div class="course-name">亀 <b>5,000円</b></div><div class="course-desc">前菜・特選造り・焼物・小鍋・揚物・酢物・上寿司・吸物・デザート</div></div></div>
    <div class="course"><div class="course-seal">宴</div><div><div class="course-name">宴 <b>7,000円</b></div><div class="course-desc">前菜・伊勢海老造り・焼物・小鍋・揚物・特上寿司・吸物・デザート</div></div></div>
  </section>

  <div class="abs band drinks-band">得々飲み放題</div>
  <div class="abs drinks-price">お一人様 <b>5,000</b>円より</div>
  <div class="abs drinks-note">2時間飲み放題付き お料理・お飲み物</div>
  <div class="abs band nabe-band">寄せ鍋</div>
  <div class="abs nabe-price"><b>3,500</b>円より</div>
  <div class="abs nabe-photo" role="img" aria-label="寄せ鍋の写真"></div>

  <div class="abs joshi"></div>
  <div class="abs joshi-kicker">わいわいがやがや</div>
  <h2 class="abs joshi-title">女子会セット</h2>
  <div class="abs joshi-note">1組4名〜20名様まで<br>承ります。</div>

  <div class="abs plan plan-sushi">
    <div class="plan-name">女子会上寿司コース</div>
    <div class="plan-price">2,500<small>円</small></div>
    <div class="plan-note">茶碗蒸し・前菜・デザート・ソフトドリンク付き</div>
  </div>
  <div class="abs side-dishes">
    <div class="side-dish" role="img" aria-label="茶碗蒸しの写真"></div>
    <div class="side-dish" role="img" aria-label="前菜の写真"></div>
    <div class="side-dish" role="img" aria-label="デザートの写真"></div>
  </div>
  <div class="abs sushi-photo" role="img" aria-label="上寿司の盛り合わせの写真"></div>

  <div class="abs gozen-photo" role="img" aria-label="女子会御膳の写真"></div>
  <div class="abs plan plan-gozen">
    <div class="plan-name">女子会御膳コース</div>
    <div class="plan-price">2,500<small>円</small></div>
    <div class="plan-note">ソフトドリンク付き</div>
  </div>
</main>
</body>
</html>
```